Medical Device Company needs website

We are a start-up medical device company looking to sell boot (foot) and brace (ankle) products on Shopify. We are still working on the name but you can use Kaltir as a placeholder- no logo yet)

Website information:
- Look: modern/tech with clean lines and symmetry.
- Colors: teal, white, black, and greys.
- Headers: home, shop, about us, help, blog
- Icons (upper right): search, my account and shopping cart
-place to sign up for newsletter

```html
<!DOCTYPE html>
<html lang="en">
<head>
<meta charset="utf-8">
<title>Kaltir — Boots &amp; Braces</title>
<link href="https://fonts.googleapis.com/css2?family=Raleway:wght@400;500;600;700;800&family=Noto+Serif:wght@400&display=swap" rel="stylesheet">
<style>
:root{
  --teal:#00bfcf;
  --teal-soft:#d6f4f7;
  --teal-mid:#9fe2e9;
  --teal-band:#b3ebf0;
  --ink:#1d1d1d;
  --grey:#777;
  --grey-light:#e3e3e3;
  --white:#fff;
}
*{box-sizing:border-box;margin:0;padding:0}
html,body{width:1200px;height:3077px;overflow:hidden}
body{position:relative;background:var(--white);font-family:"Raleway",sans-serif;color:var(--ink)}
.abs{position:absolute}
.promo-bar{left:0;top:33px;width:1200px;height:24px;background:var(--teal);color:var(--white);font-size:12px;font-weight:700;text-align:center;line-height:24px}
.site-header{left:0;top:57px;width:1200px;height:84px;background:var(--white);box-shadow:0 3px 8px rgba(0,0,0,.06);z-index:2}
.brand{font-size:38px;font-weight:500;color:var(--teal);letter-spacing:.5px}
.site-header .brand{left:84px;top:18px}
.main-nav{left:283px;top:33px;display:flex;gap:22px;font-size:14px;font-weight:700}
.main-nav .caret{display:inline-block;border:4px solid transparent;border-top-color:var(--teal);margin-left:4px;vertical-align:middle;margin-top:3px}
.search{left:755px;top:27px;width:290px;height:32px;border-radius:16px;background:#f2f2f2;font-size:12px;color:#999;padding-left:33px;line-height:32px}
.search svg{position:absolute;left:11px;top:9px}
.header-icon{top:29px}
.hero{left:0;top:141px;width:1200px;height:458px;overflow:hidden}
.hero h1{left:79px;top:86px;width:600px;font-family:"Noto Serif",serif;font-weight:400;font-size:55px;line-height:62px;color:var(--grey)}
.hero p{left:79px;top:240px;width:652px;font-size:11px;line-height:17px;color:#888;text-align:justify}
.btn{background:var(--teal);color:var(--white);font-weight:700;text-align:center;border-radius:6px}
.hero .btn{left:79px;top:323px;width:249px;height:50px;line-height:50px;font-size:13px}
.media{border-radius:8px}
.dots{display:flex;gap:4px}
.dots span{width:42px;height:4px;background:var(--grey-light)}
.dots span.on{background:var(--teal)}
.section-title{font-size:34px;font-weight:800;color:var(--teal);text-align:center}
.product{width:170px}
.product .shot{width:167px;height:165px;border-radius:6px}
.product .name{margin-top:33px;font-size:13px;color:#444}
.product .price{margin-top:10px;font-size:14px;font-weight:800}
.product .actions{margin-top:13px;display:flex;gap:9px}
.product .buy{width:116px;height:41px;line-height:41px;font-size:13px}
.product .cart{width:42px;height:41px;border:1.5px solid var(--teal);border-radius:6px;display:flex;align-items:center;justify-content:center}
.cat-panel{background:var(--teal-soft)}
.cat-card{background:var(--white);border-radius:14px}
.cat-desc{font-size:10px;line-height:17px;color:#888;text-align:center}
.testimonials{left:0;top:2239px;width:1200px;height:457px;background:var(--teal-band);overflow:hidden}
.testimonials h2{width:1200px;top:82px;text-align:center;font-size:33px;font-weight:700;color:#555}
.reviewer{width:1200px;text-align:center}
.quote{left:326px;top:208px;width:548px;font-size:11.5px;line-height:17.5px;color:#444;text-align:center}
.btn-ghost{left:475px;top:338px;width:250px;height:50px;background:var(--white);border-radius:6px;color:var(--teal);font-weight:700;font-size:13px;text-align:center;line-height:50px}
.site-footer .brand{left:84px;top:2740px;font-size:52px}
.footer-text{left:84px;top:2796px;width:292px;font-size:11px;line-height:16.5px;color:#888;text-align:justify}
.join{left:84px;top:2858px;font-size:17px;font-weight:700;color:var(--teal)}
.email{left:84px;top:2880px;width:291px;height:33px;border:1px solid #999;font-size:11px;color:#999;padding-left:12px;line-height:31px}
.signup{left:84px;top:2934px;width:115px;height:42px;line-height:42px;font-size:13px}
.foot-col h3{font-size:16px;font-weight:700;color:var(--teal);margin-bottom:13px}
.foot-col a{display:block;font-size:11.5px;font-weight:600;color:#333;text-decoration:none;margin-bottom:15px}
.social{display:flex;gap:8px;margin-top:-2px}
.social span{width:16px;height:16px;border-radius:3px;background:var(--teal)}
.legal{left:0;top:3017px;width:1200px;height:60px;background:var(--teal);color:var(--white);font-size:11px;font-weight:700;text-align:center;line-height:60px}
</style>
</head>
<body>

<div class="abs promo-bar">FREE SHIPPING OVER $75!</div>

<header class="abs site-header">
  <div class="abs brand">Kaltir</div>
  <nav class="abs main-nav">
    <span>Home</span><span>Shop<i class="caret"></i></span><span>About Us</span><span>Help</span><span>Blog</span>
  </nav>
  <div class="abs search">
    <svg width="15" height="15" viewBox="0 0 15 15" fill="none" stroke="#00bfcf" stroke-width="2"><circle cx="6" cy="6" r="4.5"/><path d="M9.5 9.5 14 14"/></svg>
    Search
  </div>
  <svg class="abs header-icon" style="left:1060px" width="22" height="24" viewBox="0 0 22 24" fill="none" stroke="#1d1d1d" stroke-width="2"><circle cx="11" cy="7" r="5"/><path d="M2 23c0-5 4-8 9-8s9 3 9 8"/></svg>
  <svg class="abs header-icon" style="left:1096px" width="24" height="24" viewBox="0 0 24 24" fill="none" stroke="#1d1d1d" stroke-width="2"><path d="M1 3h4l3 12h12l2-9H6"/><circle cx="9" cy="20" r="1.7"/><circle cx="19" cy="20" r="1.7"/><path d="M8 9h13M9 12h11"/></svg>
</header>

<section class="abs hero">
  <svg class="abs" style="left:0;top:0" width="1200" height="458" viewBox="0 0 1200 458">
    <rect width="1200" height="458" fill="#d2f2f6"/>
    <polygon points="362,0 1075,0 720,330" fill="#e4f8fa"/>
    <polygon points="1075,0 1200,0 1200,458 567,458" fill="#9fe2e9"/>
    <polygon points="720,330 870,458 567,458" fill="#b8eaef"/>
  </svg>
  <h1 class="abs">Lorem Ipsum is simply dummy text</h1>
  <p class="abs">Lorem Ipsum is simply dummy text of the printing and typesetting industry. Lorem Ipsum has been the industry's standard dummy text ever since the 1500s, when an unknown printer took a galley of type and scrambled it to make a type specimen book.</p>
  <div class="abs btn">SHOP NOW</div>
  <div class="abs media" role="img" aria-label="White walking boot with grey straps and teal sole" style="left:800px;top:32px;width:298px;height:376px;background:linear-gradient(160deg,#f4f6f8 0%,#d9dde2 60%,#00c4d4 100%);border-radius:40px 40px 30px 60px"></div>
</section>

<div class="abs dots" style="left:464px;top:609px"><span></span><span class="on"></span><span></span><span></span><span></span><span></span></div>

<h2 class="abs section-title" style="left:0;top:658px;width:1200px">OUR BEST SELLERS</h2>

<div class="abs product" style="left:141px;top:725px">
  <div class="shot" role="img" aria-label="White walking boot" style="background:linear-gradient(170deg,#f5f6f8,#d8dce0 70%,#19c6d4)"></div>
  <div class="name">Product Name 01</div><div class="price">$39.99</div>
  <div class="actions"><div class="btn buy">BUY NOW</div><div class="cart"><svg width="20" height="18" viewBox="0 0 24 22" fill="none" stroke="#00bfcf" stroke-width="2"><path d="M1 2h4l3 12h12l2-9H6"/><circle cx="9" cy="19" r="1.6"/><circle cx="19" cy="19" r="1.6"/></svg></div></div>
</div>
<div class="abs product" style="left:392px;top:725px">
  <div class="shot" role="img" aria-label="Black ankle sleeve on a foot" style="background:linear-gradient(170deg,#fff,#3a3a3a 55%,#c99b7a)"></div>
  <div class="name">Product Name 02</div><div class="price">$39.99</div>
  <div class="actions"><div class="btn buy">BUY NOW</div><div class="cart"><svg width="20" height="18" viewBox="0 0 24 22" fill="none" stroke="#00bfcf" stroke-width="2"><path d="M1 2h4l3 12h12l2-9H6"/><circle cx="9" cy="19" r="1.6"/><circle cx="19" cy="19" r="1.6"/></svg></div></div>
</div>
<div class="abs product" style="left:641px;top:725px">
  <div class="shot" role="img" aria-label="Grey and blue air walker boot" style="background:linear-gradient(170deg,#f4f5f7,#b8c2cc 60%,#e9eef2)"></div>
  <div class="name">Product Name 03</div><div class="price">$39.99</div>
  <div class="actions"><div class="btn buy">BUY NOW</div><div class="cart"><svg width="20" height="18" viewBox="0 0 24 22" fill="none" stroke="#00bfcf" stroke-width="2"><path d="M1 2h4l3 12h12l2-9H6"/><circle cx="9" cy="19" r="1.6"/><circle cx="19" cy="19" r="1.6"/></svg></div></div>
</div>
<div class="abs product" style="left:891px;top:725px">
  <div class="shot" role="img" aria-label="Black and green ankle wrap being fitted" style="background:linear-gradient(170deg,#fff,#2b2b2b 45%,#35c24a 70%,#e6c0a8)"></div>
  <div class="name">Product Name 04</div><div class="price">$39.99</div>
  <div class="actions"><div class="btn buy">BUY NOW</div><div class="cart"><svg width="20" height="18" viewBox="0 0 24 22" fill="none" stroke="#00bfcf" stroke-width="2"><path d="M1 2h4l3 12h12l2-9H6"/><circle cx="9" cy="19" r="1.6"/><circle cx="19" cy="19" r="1.6"/></svg></div></div>
</div>

<div class="abs dots" style="left:533px;top:1049px"><span></span><span class="on"></span><span></span></div>

<!-- Boots -->
<div class="abs cat-panel" style="left:0;top:1105px;width:599px;height:543px;border-radius:0 36px 0 0"></div>
<div class="abs cat-card" style="left:107px;top:1156px;width:442px;height:440px">
  <div class="abs media" role="img" aria-label="White walking boot with teal sole" style="left:90px;top:22px;width:290px;height:380px;background:linear-gradient(160deg,#f6f7f9,#d5d9de 65%,#00c4d4);border-radius:40px 40px 30px 60px"></div>
</div>
<h2 class="abs section-title" style="left:682px;top:1155px;width:400px">BOOTS</h2>
<p class="abs cat-desc" style="left:670px;top:1207px;width:424px">Lorem Ipsum is simply dummy text of the printing and typesetting industry. Lorem Ipsum has been the industry's standard dummy text ever since the 1500s.</p>
<div class="abs product" style="left:675px;top:1266px">
  <div class="shot" role="img" aria-label="Black tall walking boot" style="width:120px;margin-left:20px;background:linear-gradient(170deg,#fff,#2a2a2a 40%,#444)"></div>
  <div class="name" style="margin-top:19px">Product Name 01</div><div class="price">$29.99</div>
  <div class="actions"><div class="btn buy">BUY NOW</div><div class="cart"><svg width="20" height="18" viewBox="0 0 24 22" fill="none" stroke="#00bfcf" stroke-width="2"><path d="M1 2h4l3 12h12l2-9H6"/><circle cx="9" cy="19" r="1.6"/><circle cx="19" cy="19" r="1.6"/></svg></div></div>
</div>
<div class="abs product" style="left:924px;top:1266px">
  <div class="shot" role="img" aria-label="White tall walking boot" style="width:120px;margin-left:20px;background:linear-gradient(170deg,#f6f7f9,#cfd4d9 70%,#1bc7d5)"></div>
  <div class="name" style="margin-top:19px">Product Name 02</div><div class="price">$39.99</div>
  <div class="actions"><div class="btn buy">BUY NOW</div><div class="cart"><svg width="20" height="18" viewBox="0 0 24 22" fill="none" stroke="#00bfcf" stroke-width="2"><path d="M1 2h4l3 12h12l2-9H6"/><circle cx="9" cy="19" r="1.6"/><circle cx="19" cy="19" r="1.6"/></svg></div></div>
</div>
<div class="abs dots" style="left:816px;top:1576px"><span></span><span class="on"></span><span></span></div>

<!-- Braces -->
<div class="abs cat-panel" style="left:599px;top:1648px;width:601px;height:543px;border-radius:36px 0 0 36px"></div>
<div class="abs cat-card" style="left:650px;top:1700px;width:441px;height:440px">
  <div class="abs media" role="img" aria-label="Hands pulling a black ankle sleeve onto a foot" style="left:60px;top:0;width:320px;height:440px;background:linear-gradient(180deg,#8a5a3e 0%,#6b442e 20%,#151515 30%,#1e1e1e 75%,#c6946f 90%,#fff 100%);border-radius:0"></div>
</div>
<h2 class="abs section-title" style="left:115px;top:1698px;width:400px">BRACES</h2>
<p class="abs cat-desc" style="left:103px;top:1750px;width:424px">Lorem Ipsum is simply dummy text of the printing and typesetting industry. Lorem Ipsum has been the industry's standard dummy text ever since the 1500s.</p>
<div class="abs product" style="left:107px;top:1809px">
  <div class="shot" role="img" aria-label="Black tall walking boot" style="width:120px;margin-left:20px;background:linear-gradient(170deg,#fff,#2a2a2a 40%,#444)"></div>
  <div class="name" style="margin-top:19px">Product Name 01</div><div class="price">$29.99</div>
  <div class="actions"><div class="btn buy">BUY NOW</div><div class="cart"><svg width="20" height="18" viewBox="0 0 24 22" fill="none" stroke="#00bfcf" stroke-width="2"><path d="M1 2h4l3 12h12l2-9H6"/><circle cx="9" cy="19" r="1.6"/><circle cx="19" cy="19" r="1.6"/></svg></div></div>
</div>
<div class="abs product" style="left:358px;top:1809px">
  <div class="shot" role="img" aria-label="White tall walking boot" style="width:120px;margin-left:20px;background:linear-gradient(170deg,#f6f7f9,#cfd4d9 70%,#1bc7d5)"></div>
  <div class="name" style="margin-top:19px">Product Name 02</div><div class="price">$39.99</div>
  <div class="actions"><div class="btn buy">BUY NOW</div><div class="cart"><svg width="20" height="18" viewBox="0 0 24 22" fill="none" stroke="#00bfcf" stroke-width="2"><path d="M1 2h4l3 12h12l2-9H6"/><circle cx="9" cy="19" r="1.6"/><circle cx="19" cy="19" r="1.6"/></svg></div></div>
</div>
<div class="abs dots" style="left:250px;top:2119px"><span></span><span class="on"></span><span></span></div>

<!-- Testimonials -->
<section class="abs testimonials">
  <div class="abs" role="img" aria-label="Faded white walking boot" style="left:-20px;top:0;width:300px;height:430px;background:linear-gradient(150deg,#e9f9fb 10%,#d3eff3 60%,#5fd6e0 95%);opacity:.8;border-radius:0 80px 60px 0"></div>
  <div class="abs" role="img" aria-label="Faded grey ankle sleeve on a foot" style="left:915px;top:0;width:270px;height:420px;background:linear-gradient(200deg,#9fb5b8 0%,#7f9a9e 60%,#e8dccf 95%);opacity:.75;border-radius:0 0 40px 120px"></div>
  <h2 class="abs">Testimonials</h2>
  <div class="abs reviewer" style="top:126px;font-size:16px;font-weight:700;color:#444">Dana R.</div>
  <div class="abs reviewer" style="top:149px;font-size:10px;color:#555">September 10</div>
  <svg class="abs" style="left:540px;top:167px" width="120" height="22" viewBox="0 0 120 22" fill="#00bfcf">
    <g id="s"><polygon points="11,1 14,8 21,8 15.5,12.5 17.5,20 11,15.5 4.5,20 6.5,12.5 1,8 8,8"/></g>
    <use href="#s" x="24"/><use href="#s" x="48"/><use href="#s" x="72"/><use href="#s" x="96"/>
  </svg>
  <div class="abs" style="left:322px;top:199px;width:556px;height:1px;background:#8fc9ce"></div>
  <p class="abs quote">Lorem Ipsum is simply dummy text of the printing and typesetting industry. Lorem Ipsum has been the industry's standard dummy text ever since the 1500s, when an unknown printer took a galley of type and scrambled it to make a type specimen book. It has survived not only five centuries, but also the leap into electronic typesetting, remaining essentially unchanged. It was popularised in the 1960s with the release of Typeset sheets containing Lorem Ipsum passages, and more recently with desktop publishing software like Folio Layout including versions of Lorem Ipsum.</p>
  <svg class="abs" style="left:274px;top:209px" width="16" height="26" viewBox="0 0 16 26" fill="none" stroke="#fff" stroke-width="2.5"><path d="M13 2 3 13l10 11"/></svg>
  <svg class="abs" style="left:910px;top:209px" width="16" height="26" viewBox="0 0 16 26" fill="none" stroke="#fff" stroke-width="2.5"><path d="m3 2 10 11L3 24"/></svg>
  <div class="abs btn-ghost">SHOW ALL</div>
</section>

<!-- Footer -->
<footer class="site-footer">
  <div class="abs brand">Kaltir</div>
  <p class="abs footer-text">Lorem Ipsum is simply dummy text of the printing and typesetting industry. Lorem Ipsum has been the industry's standard dummy text ever since the 1500s</p>
  <div class="abs join">Join Us</div>
  <div class="abs email">Your Email Address</div>
  <div class="abs btn signup">SIGN UP</div>
  <div class="abs foot-col" style="left:481px;top:2755px"><h3>SHOP</h3><a>Boots</a><a>Braces</a></div>
  <div class="abs foot-col" style="left:636px;top:2755px"><h3>ABOUT</h3><a>About Us</a><a>Contact Us</a><a>Blogs</a></div>
  <div class="abs foot-col" style="left:805px;top:2755px"><h3>HELP</h3><a>FAQs</a><a>Shipping &amp; Returns</a><a>Privacy Policy</a><a>Terms of Service</a></div>
  <div class="abs foot-col" style="left:1016px;top:2755px"><h3 style="color:#333">FOLLOW US</h3>
    <div class="social"><span role="img" aria-label="Social profile one"></span><span role="img" aria-label="Social profile two"></span></div>
  </div>
  <div class="abs legal">2024© All right reserved by Kaltir</div>
</footer>

</body>
</html>
```